This flyer needs to be created via canva and all elements editable.
Lanternfield Crown Hotel Corvell Bay Strand Triathlon Race 1: Sun 8th December 2024 10:00am

Welcome to the Lanternfield Crown Hotel Corvell Bay Strand Triathlon brought to you by Harbourline Multisport.

Registration link: https://entries.velmoraclub.example/events/details/4K7Q2M9X/

Please note: Entries close at 8pm on the Saturday night before the Race.
This event is a Harbourline Multisport Club ‘Triathlete of the Year’ points race.

We are also very lucky to have PKD Minnows at the Lanternfield Crown Hotel Corvell Bay Strand Triathlon Race racing starts for Minnows at 9.00am

The Race Lowdown:
When:
* Race 1: Sun 8th December 2024 at 10:00am - Sprint and Short Course Triathlon, and a Sprint Duathlon and AquaBike, plus Minnows.

The other races organised by Harbourline Multisport which contribute towards the Club Triathlon of the Year are on:
* Race 2: Sunday, 19th January 2025 at 9:30am – Olympic, Sprint, and Short Course Triathlon, and a Sprint Duathlon and AquaBike (WQE), plus Minnows
* Race 3: Saturday, 22th March 2024 at 10:00am - Sprint and Short Course Triathlon, and a Sprint Duathlon and AquaBike, plus Minnows. (incorporating Meridian Uniformed Responders Carnival 2025)

Where:
Corvell Bay Strand Day Use Area 2, off Kestrel Lane.

More information visit the Harbourline Multisport Club website https://www.harbourlinemultisport.example/

```html
<!DOCTYPE html>
<html lang="en">
<head>
<meta charset="utf-8">
<title>Race Lowdown Flyer</title>
<link rel="stylesheet" href="https://fonts.googleapis.com/css2?family=Roboto:wght@400;500;700;900&display=swap">
<style>
:root{
  --page-bg:#e9e9ea;
  --paper:#ffffff;
  --ink:#111111;
  --blue:#0a84d0;
  --magenta:#e8168c;
  --teal:#00afa6;
  --bar-grey:#3d3f44;
  --bar-black:#0d0d0d;
  --navy:#1a2a4a;
}
*{box-sizing:border-box;margin:0;padding:0}
html,body{width:1200px;height:2400px;overflow:hidden}
body{background:var(--page-bg);font-family:"Roboto",Arial,sans-serif;color:var(--ink);position:relative}
.flyer{position:absolute;left:50px;top:425px;width:1100px;height:1551px;background:var(--paper);box-shadow:0 20px 50px rgba(0,0,0,.18)}
.abs{position:absolute}
.brand-club{left:85px;top:58px;display:flex;align-items:center;gap:16px;font-size:40px;font-weight:700;color:var(--navy);line-height:1}
.brand-club .dot{width:46px;height:46px;border-radius:50%;background:var(--magenta)}
.brand-hotel{left:560px;top:80px;width:180px;text-align:center;font-size:24px;font-weight:700;color:var(--navy);line-height:1.15}
.photo{position:absolute;top:240px;height:624px;width:271px}
.photo-run{left:121px;clip-path:polygon(0 4%,100% 7%,100% 100%,0 100%);background:linear-gradient(180deg,#6aa9dc 0%,#4d7a8c 45%,#4a5a3a 75%,#2e3a2c 100%)}
.photo-swim{left:416px;clip-path:polygon(0 0,100% 3%,100% 100%,0 100%);background:linear-gradient(180deg,#5f8a45 0%,#3a3a3e 45%,#9a1f35 80%,#2a2a2a 100%)}
.photo-bike{left:715px;clip-path:polygon(0 1%,100% 4%,100% 100%,0 100%);background:linear-gradient(180deg,#9aa68c 0%,#4b5240 40%,#2a2d30 70%,#5a5e62 100%)}
.heading{left:98px;top:906px;font-size:46px;font-weight:900;letter-spacing:.5px}
.races{left:78px;top:976px;width:976px;height:306px;display:flex}
.race{padding:28px 30px 0 38px;color:#fff}
.race-1{width:331px;background:var(--blue)}
.race-2{width:312px;background:var(--magenta);padding-left:30px}
.race-3{width:333px;background:var(--teal);padding-left:32px}
.race h3{font-size:32px;font-weight:700;margin-bottom:10px}
.race p{font-size:21px;line-height:1.25}
.reg-bar{left:78px;top:1297px;width:960px;height:64px;display:flex}
.reg-label{width:307px;background:var(--bar-grey);color:#fff;font-size:26px;font-weight:700;display:flex;align-items:center;padding-left:24px}
.reg-url{flex:1;background:var(--bar-black);color:#fff;font-size:17px;font-weight:500;display:flex;align-items:center;padding-left:20px}
.info-text{left:98px;top:1390px;font-size:26px;font-weight:700;line-height:1.22}
.info-pill{left:90px;top:1464px;height:38px;padding:0 22px 0 14px;background:var(--bar-black);color:#fff;border-radius:19px;display:flex;align-items:center;gap:12px;font-size:22px;font-weight:700}
.divider{left:594px;top:1396px;width:3px;height:144px;background:var(--blue)}
.venue{left:625px;top:1430px;display:flex;gap:16px;align-items:flex-start}
.venue p{font-size:26px;font-weight:700;line-height:1.2}
</style>
</head>
<body>
<main class="flyer">
  <div class="abs brand-club"><span class="dot"></span>Harbourline Multisport</div>
  <div class="abs brand-hotel">Lanternfield Crown Hotel</div>

  <div class="photo photo-run" role="img" aria-label="Photo of a triathlete running along the coast wearing race number 58"></div>
  <div class="photo photo-swim" role="img" aria-label="Photo of a triathlete in a swim cap leaving the water in a wetsuit"></div>
  <div class="photo photo-bike" role="img" aria-label="Photo of a triathlete riding a road bike in a helmet"></div>

  <h2 class="abs heading">THE RACE LOWDOWN</h2>

  <section class="abs races">
    <div class="race race-1">
      <h3>RACE 1</h3>
      <p>Sun 8th December 2024 at 10:00am - Sprint and Short Course Triathlon, and a Sprint Duathlon and Aqua-Bike, plus Minnows.</p>
    </div>
    <div class="race race-2">
      <h3>RACE 2</h3>
      <p>Sunday, 19th January 2025 at 9:30am – Olympic, Sprint, and Short Course Triathlon, and a Sprint Du-athlon and AquaBike (WQE), plus Minnows</p>
    </div>
    <div class="race race-3">
      <h3>RACE 3</h3>
      <p>Saturday, 22th March 2024 at 10:00am - Sprint and Short Course Triathlon, and a Sprint Duathlon and AquaBike, plus Minnows. (incorporating Meridian Uniformed Responders Carnival 2025)</p>
    </div>
  </section>

  <div class="abs reg-bar">
    <div class="reg-label">REGISTRATION LINK:</div>
    <div class="reg-url">https://entries.velmoraclub.example/events/details/4K7Q2M9X/</div>
  </div>

  <p class="abs info-text">More information visit the Harbourline<br>Multisport club website</p>
  <div class="abs info-pill">
    <svg width="20" height="20" viewBox="0 0 20 20" fill="none" stroke="#fff" stroke-width="1.6"><circle cx="10" cy="10" r="8.5"/><ellipse cx="10" cy="10" rx="3.8" ry="8.5"/><path d="M1.5 10h17M3 5.5h14M3 14.5h14"/></svg>
    https://www.harbourlinemultisport.example/
  </div>

  <div class="abs divider"></div>

  <div class="abs venue">
    <svg width="30" height="38" viewBox="0 0 30 38" fill="none" stroke="#111" stroke-width="2.4"><path d="M15 36C15 36 3 22 3 13.5a12 12 0 0 1 24 0C27 22 15 36 15 36z"/><circle cx="15" cy="13.5" r="4.5"/></svg>
    <p>Corvell Bay Strand Day Use<br>Area 2, off Kestrel Lane.</p>
  </div>
</main>
</body>
</html>
```